Redesign my business cards

I would like pretty much all the same information as my current business cards but redesigned to stand out more and be more unique photo uploaded to show my current business cards don’t mind if you want to remove or replace I for on the back

```html
<!DOCTYPE html>
<html lang="en">
<head>
<meta charset="utf-8">
<title>Brightlane Detailing – Business Card</title>
<link rel="stylesheet" href="https://fonts.googleapis.com/css2?family=Poppins:wght@300;400;600;800&display=swap">
<style>
  :root {
    --backdrop: #e8e8e8;
    --card: #03202f;
    --card-deep: #021824;
    --cyan: #3fc4e0;
    --blue: #2a6fd0;
    --coral: #e9545f;
    --coral-soft: rgba(233, 84, 95, 0.16);
    --ink-light: #e6edf1;
    --ink-muted: #b3c2cb;
    --rule: rgba(63, 196, 224, 0.22);
  }
  * { margin: 0; padding: 0; box-sizing: border-box; }
  html, body {
    width: 1200px; height: 931px; overflow: hidden;
    background: var(--backdrop);
    font-family: "Poppins", sans-serif;
  }
  .canvas { position: relative; width: 1200px; height: 931px; }

  .card {
    position: absolute;
    width: 680px; height: 415px;
    background: var(--card);
    border-radius: 28px;
    box-shadow: 0 14px 30px rgba(0, 0, 0, 0.18);
    overflow: hidden;
  }
  .card--back { left: 470px; top: 36px; }
  .card--front { left: 50px; top: 480px; }

  /* ---------- back: services ---------- */
  .card__accent {
    position: absolute; left: 0; right: 0; bottom: 0; height: 10px;
    background: linear-gradient(90deg, var(--coral), var(--cyan), var(--blue));
  }
  .services {
    display: grid; grid-template-columns: repeat(3, 1fr);
    height: 100%; padding: 44px 28px 40px;
  }
  .service {
    text-align: center; padding: 0 18px;
    border-left: 1px solid var(--rule);
  }
  .service:first-child { border-left: none; }
  .service__icon {
    width: 84px; height: 84px; margin: 0 auto 18px;
    border-radius: 50%; background: var(--coral-soft);
    border: 2px solid var(--coral);
  }
  .service__title {
    color: var(--cyan); font-weight: 800; font-size: 20px;
    text-transform: uppercase; letter-spacing: 0.5px;
  }
  .service__bar {
    width: 36px; height: 3px; margin: 8px auto 12px;
    background: var(--coral); border-radius: 2px;
  }
  .service__text {
    color: var(--ink-muted); font-weight: 300; font-size: 12.5px; line-height: 1.45;
  }

  /* ---------- front: identity ---------- */
  .brand-panel {
    position: absolute; top: 0; right: 0; width: 250px; height: 100%;
    background: linear-gradient(160deg, var(--cyan), var(--blue));
    clip-path: polygon(70px 0, 100% 0, 100% 100%, 0 100%);
    display: flex; flex-direction: column; align-items: center; justify-content: center;
    gap: 16px; padding-left: 50px;
  }
  .brand-panel__mark {
    width: 86px; height: 86px; border-radius: 50%;
    background: var(--card-deep);
  }
  .brand-panel__name {
    color: var(--card-deep); font-weight: 800; font-size: 17px;
    text-transform: uppercase; letter-spacing: 2px; text-align: center; line-height: 1.3;
  }

  .contact { position: absolute; left: 48px; top: 70px; width: 400px; }
  .contact__name {
    color: var(--cyan); font-weight: 800; font-size: 40px;
    text-transform: uppercase; line-height: 1.05; letter-spacing: 0.5px;
  }
  .contact__role {
    color: var(--ink-light); font-weight: 300; font-size: 18px;
    letter-spacing: 3px; text-transform: uppercase; margin-top: 6px;
  }
  .contact__rule {
    width: 60px; height: 4px; background: var(--coral);
    border-radius: 2px; margin: 26px 0 28px;
  }
  .contact__line {
    display: flex; align-items: center; gap: 12px;
    color: var(--ink-light); font-weight: 400; font-size: 16px; margin-bottom: 14px;
    white-space: nowrap;
  }
  .contact__icon {
    width: 34px; height: 34px; flex: none; border-radius: 50%;
    border: 1.5px solid var(--coral);
    display: flex; align-items: center; justify-content: center;
  }
  .contact__icon svg { width: 16px; height: 16px; }
</style>
</head>
<body>
<main class="canvas">

  <section class="card card--back" aria-label="Services">
    <div class="services">
      <article class="service">
        <div class="service__icon" role="img" aria-label="Icon of a car seat being sprayed with cleaner"></div>
        <h2 class="service__title">Interior</h2>
        <div class="service__bar"></div>
        <p class="service__text">Vacuum &amp; deep clean of carpets &amp; upholstery or leather treatment, interior trim clean &amp; condition, window polish and treatment, steam clean and stain removal</p>
      </article>
      <article class="service">
        <div class="service__icon" role="img" aria-label="Icon of a car front being sprayed"></div>
        <h2 class="service__title">Exterior</h2>
        <div class="service__bar"></div>
        <p class="service__text">Extreme wash &amp; polish, exterior trim reviver &amp; protector, window polish &amp; treatment, tyre dressing, engine bay cleaned</p>
      </article>
      <article class="service">
        <div class="service__icon" role="img" aria-label="Icon of shining sparkles"></div>
        <h2 class="service__title">Full Extreme</h2>
        <div class="service__bar"></div>
        <p class="service__text">Extreme wash &amp; polish, tyre dressing, engine bay cleaned, vacuum &amp; deep clean of carpets &amp; upholstery or leather treatment, interior &amp; exterior trim reviver &amp; protector, window polish and treatment</p>
      </article>
    </div>
    <div class="card__accent"></div>
  </section>

  <section class="card card--front" aria-label="Contact">
    <div class="contact">
      <h1 class="contact__name">Sam<br>Harlow</h1>
      <p class="contact__role">Owner / Operator</p>
      <div class="contact__rule"></div>
      <p class="contact__line">
        <span class="contact__icon">
          <svg viewBox="0 0 24 24" fill="none" stroke="var(--cyan)" stroke-width="2" stroke-linecap="round" stroke-linejoin="round" aria-hidden="true"><path d="M5 3h4l2 5-2.5 1.5a11 11 0 0 0 6 6L16 13l5 2v4a2 2 0 0 1-2 2A16 16 0 0 1 3 5a2 2 0 0 1 2-2z"/></svg>
        </span>
        0400 127 583
      </p>
      <p class="contact__line">
        <span class="contact__icon">
          <svg viewBox="0 0 24 24" fill="none" stroke="var(--cyan)" stroke-width="2" stroke-linejoin="round" aria-hidden="true"><rect x="3" y="5" width="18" height="14" rx="2"/><path d="M3 7l9 6 9-6"/></svg>
        </span>
        hello@brightlanedetailing.example
      </p>
    </div>
    <div class="brand-panel">
      <span class="brand-panel__mark"></span>
      <p class="brand-panel__name">Brightlane<br>Detailing</p>
    </div>
  </section>

</main>
</body>
</html>
```